International Clinical Software Company needs a new business card design

We are looking for a new business card design for our company that has recently expanded into the UK market, making us a multinational company.
After having rebranded our website and produced a new style guide, we are looking for a business card that is creative and attention grabbing, while being consistent with the style and colour scheme used on the new website, www.pennick.care
We produce care management technology for the aged care market, but the main aspect we aim to communicate is the human element of our software, and the way it assists in providing better care for aged people, and stronger relationships between aged people and the staff that care for them.
Our current business card is a dark green with gold text, which makes the text quite difficult to read, not very aesthetically appealing and the colour scheme looks quite dated.
We would like something fresh and modern, that can still be colourful but doesn't use large blocks of dark colour, and uses the colours within our logo.
Something tying in with the leaves that are used in our logo could work quite nicely, along with the Autumn/Fall colours of soft greens, yellows and reds (also in our existing logo). However also happy to look at fresh, completely out of the box ideas we may not have yet considered.
Target Market(s)
The people that receive this business card work in the aged card or health industry and are either corporate/management level staff or clinical (Registered Nurses, care workers etc.)
Industry/Entity Type
Health Product
Contact Information for Business Card
Company Name - PennickCare
Company locations: United Kingdom, Australia, New Zealand
Staff Details:
Staff name: Dermot Marlow
Staff job title: Executive Chairman
Staff email: d.marlow@pennick.care
Office phone number: 01632 960481
Other font styles liked:
- Calibri
Requirements
Must have
- Must include the PennickCare brand name in it's current font
- Must include logo (3 leaves in gold circle)
- Must include Business Card Details
Nice to have
- Elements of gold
- White space
- Something autumn themed but not too cliched
Should not have
- No blue - used by a major competitor and we would like to differentiate from them
- Large blocks of dark green colour (the green that appears in our leaves on the logo on our current business card is the background colour and it is far too dark)

```html
<!DOCTYPE html>
<html lang="en">
<head>
<meta charset="utf-8">
<title>PennickCare Business Card</title>
<link rel="stylesheet" href="https://fonts.googleapis.com/css2?family=Open+Sans:ital,wght@0,300;0,400;0,700;1,700&display=swap">
<style>
  :root {
    --backdrop: #b4bccb;
    --card: #ffffff;
    --gold: #a79b70;
    --leaf-green: #4a6a17;
    --olive: #9b9400;
    --berry: #8c0029;
  }
  html, body {
    margin: 0;
    padding: 0;
    width: 1200px;
    height: 1000px;
    overflow: hidden;
    background: var(--backdrop);
  }
  .card {
    position: absolute;
    left: 88px;
    top: 201px;
    width: 1050px;
    height: 599px;
    background: var(--card);
    overflow: hidden;
    font-family: "Open Sans", "Calibri", sans-serif;
  }
  .autumn-bands {
    position: absolute;
    left: 0;
    top: 0;
    width: 1050px;
    height: 599px;
  }
  .brand-mark {
    position: absolute;
    left: 76px;
    top: 77px;
    width: 100px;
    height: 100px;
    border: 3px solid var(--gold);
    border-radius: 50%;
    box-sizing: border-box;
  }
  .brand-name {
    position: absolute;
    left: 200px;
    top: 88px;
    margin: 0;
    font-weight: 300;
    font-size: 38px;
    line-height: 1;
    color: var(--gold);
  }
  .brand-regions {
    position: absolute;
    left: 200px;
    top: 148px;
    margin: 0;
    font-weight: 400;
    font-size: 22px;
    line-height: 1;
    color: var(--gold);
  }
  .brand-regions .divider {
    padding: 0 4px;
  }
  .contact {
    position: absolute;
    left: 610px;
    top: 302px;
    margin: 0;
    padding: 0;
    list-style: none;
    color: var(--leaf-green);
    font-size: 28px;
    line-height: 40px;
  }
  .contact li {
    display: flex;
    align-items: center;
  }
  .contact .icon {
    width: 32px;
    height: 32px;
    margin-right: 23px;
    flex: none;
  }
  .person {
    position: absolute;
    right: 566px;
    top: 428px;
    text-align: right;
  }
  .person-name {
    margin: 0;
    font-weight: 700;
    font-size: 46px;
    line-height: 56px;
    color: var(--leaf-green);
  }
  .person-title {
    margin: 0;
    font-weight: 700;
    font-style: italic;
    font-size: 38px;
    line-height: 50px;
    color: var(--gold);
  }
</style>
</head>
<body>
  <main class="card">
    <svg class="autumn-bands" viewBox="0 0 1050 599" aria-hidden="true">
      <polygon points="572,599 897,454 1050,454 1050,599" fill="var(--leaf-green)"/>
      <polygon points="830,549 1050,224 1050,599" fill="var(--olive)"/>
      <polygon points="710,599 1050,455 1050,599" fill="var(--berry)"/>
    </svg>

    <div class="brand-mark" aria-hidden="true"></div>
    <h1 class="brand-name">PennickCare</h1>
    <p class="brand-regions">United Kingdom<span class="divider">|</span>Australia<span class="divider">|</span>New Zealand</p>

    <ul class="contact">
      <li>
        <svg class="icon" viewBox="0 0 32 32" aria-hidden="true">
          <rect x="1" y="9" width="30" height="17" fill="var(--leaf-green)"/>
          <polyline points="1,9 16,19 31,9" fill="none" stroke="#ffffff" stroke-width="2"/>
        </svg>
        d.marlow@pennick.care
      </li>
      <li>
        <svg class="icon" viewBox="0 0 32 32" aria-hidden="true">
          <rect x="8" y="2" width="15" height="28" rx="2" fill="none" stroke="var(--leaf-green)" stroke-width="3"/>
          <line x1="13" y1="25" x2="18" y2="25" stroke="var(--leaf-green)" stroke-width="2"/>
        </svg>
        01632 960481
      </li>
    </ul>

    <div class="person">
      <h2 class="person-name">Dermot Marlow</h2>
      <p class="person-title">Executive Chairman</p>
    </div>
  </main>
</body>
</html>
```